FixyFellas,com Home Maintenance Membership Website

Fixy Fellas is a yearly home maintenance membership website where Home Owners, Contractor, and Subcontractors can interact in an online bidding environment to exchange goods and services.

Our Tag Line Is: We Tackle The Weekend Lists That Other Fellas Won't Tackle
Updates

Target Market(s)

Homeowner, Female, 26 to 56 years of age. Middle to upper income.
Contractors/Subcontractors

Industry/Entity Type

Environment

Font styles to use
Other font styles liked:
• We want to match the logo font

Requirements
Must have
• Three-tiered membership plans for homeowners. Features and pricing TBD
Three major customer components as well as a administration back end. The three main components will be Home Owners Page, Contractors/Subcontractors pages, and the request-for Work Pages.
Need Membership levels panel similar to the uploaded picture
We did like this site as a start point. http://www.coatguardprime.example/
Nice to have
• #1: Customer domain profiles for contractors
#2: Blog
#3: Affiliate Program
#4: Contractor Rating System
#5: Internal Messaging System
#6: Banner Ads
#7: Escrow Payments

```html
<!DOCTYPE html>
<html lang="en">
<head>
<meta charset="utf-8">
<title>Fixy Fellas — Home Maintenance Membership</title>
<link rel="stylesheet" href="https://fonts.googleapis.com/css2?family=Arimo:wght@400;700&family=Open+Sans:wght@300;400;600;700&display=swap">
<style>
:root{
  --orange:#e8561a;
  --orange-bright:#f06a1c;
  --orange-deep:#d9480f;
  --ink:#3a3a3a;
  --grey-text:#8a8a8a;
  --light-grey:#b5b5b5;
  --rule:#e3e3e3;
  --dark:#2b2b2b;
  --dark-2:#1e1e1e;
  --panel-grey:#dcdcdc;
  --white:#ffffff;
}
*{box-sizing:border-box;margin:0;padding:0}
html,body{width:1200px;height:2473px;overflow:hidden}
body{position:relative;background:var(--white);font-family:"Arimo",Arial,sans-serif;color:var(--ink)}
.abs{position:absolute}

/* header */
.top-rule{left:0;top:0;width:1200px;height:5px;background:var(--orange)}
.brand{left:132px;top:40px;display:flex;align-items:center;gap:12px}
.brand-dot{width:58px;height:58px;border-radius:50%;background:var(--orange)}
.brand-name{font-size:24px;font-weight:700;color:var(--dark)}
.social-top{left:912px;top:31px;display:flex;gap:8px}
.social-top span,.social-foot span{display:block;border-radius:50%}
.social-top span{width:27px;height:27px;background:#a9a9a9}
.main-nav{left:392px;top:84px;display:flex;align-items:center;font-size:12.5px;color:#666;text-transform:uppercase}
.main-nav a{color:inherit;text-decoration:none;margin-right:34px}
.main-nav a.current{background:var(--orange);color:var(--white);border-radius:14px;padding:7px 23px;margin-right:17px}

/* hero */
.hero{left:0;top:148px;width:1200px;height:508px;background:linear-gradient(100deg,#a8876b 0%,#c9b59f 35%,#8e6a4c 62%,#6b4a2f 100%)}
.hero-caption{left:132px;top:420px;width:494px;height:119px;background:rgba(40,40,40,.72);padding:14px 19px;color:var(--white)}
.hero-caption h1{font-size:33px;font-weight:700;letter-spacing:.5px}
.hero-caption p{font-size:11px;line-height:19px;margin-top:8px;width:440px;color:#e6e6e6}
.hero-arrows{left:566px;top:500px;display:flex;gap:12px}

/* welcome */
.welcome-title{left:0;top:694px;width:1200px;text-align:center;font-size:23px;font-weight:700;color:#555}
.accent{color:var(--orange)}
.welcome-text{left:214px;top:740px;width:775px;text-align:center;font-size:11px;line-height:24px;color:var(--light-grey)}

/* blog */
.section-title{font-size:23px;font-weight:700;color:#555}
.blog-title{left:133px;top:854px}
.blog-arrows{left:1036px;top:858px;display:flex;gap:10px}
.blog-card{top:906px;width:294px;height:238px}
.blog-card--1{left:130px;background:linear-gradient(135deg,#5b4a3a,#3a2e24)}
.blog-card--2{left:453px;background:linear-gradient(135deg,#c9b48a,#7d5a3a 60%,#d6c79d)}
.blog-card--3{left:775px;background:linear-gradient(135deg,#e8e4df,#c7c0b8 50%,#f2efe9)}
.blog-overlay{left:130px;top:906px;width:294px;height:238px;background:rgba(40,34,28,.55);color:var(--white);text-align:center;padding-top:70px}
.blog-overlay h3{font-size:18px;font-weight:700}
.blog-overlay p{font-size:12px;line-height:22px;margin-top:8px}
.blog-tools{display:flex;justify-content:center;gap:14px;margin-top:14px}
.blog-tools span{width:30px;height:28px;background:#e6e6e6;border-radius:3px;display:flex;align-items:center;justify-content:center}
.blog-label{top:1088px;width:266px;height:44px;background:rgba(50,50,50,.78);color:var(--white);font-size:12px;font-weight:700;display:flex;align-items:center;justify-content:center}

/* pricing */
.pricing-band{left:0;top:1196px;width:1200px;height:407px;background:radial-gradient(circle at 15% 30%,#f58a3c 0,transparent 18%),radial-gradient(circle at 88% 25%,#f38a40 0,transparent 14%),linear-gradient(180deg,var(--orange-bright),var(--orange-deep))}
.pricing-title{left:0;top:1230px;width:1200px;text-align:center;font-size:30px;font-weight:700;color:var(--white)}
.plan{width:242px;background:linear-gradient(90deg,#cfcfcf,#ececec 50%,#cfcfcf)}
.plan--regular{left:242px;top:1320px;height:481px}
.plan--big{left:483px;top:1307px;height:511px;box-shadow:0 6px 14px rgba(0,0,0,.35);z-index:2}
.plan--frequent{left:725px;top:1320px;height:481px}
.plan-name{height:28px;background:var(--dark-2);color:var(--white);font-size:12.5px;text-align:center;line-height:28px;text-transform:uppercase}
.plan-price{height:112px;background:linear-gradient(180deg,#3a3a3a,#1f1f1f);color:var(--white);font-family:"Open Sans",Arial,sans-serif;display:flex;align-items:center;justify-content:center;font-weight:300}
.plan--big .plan-name{height:33px;line-height:33px}
.plan--big .plan-price{height:120px;background:linear-gradient(180deg,#f58a2c,#e8561a)}
.plan-price .cur{font-size:36px;align-self:flex-start;margin-top:26px}
.plan-price .num{font-size:66px;line-height:1}
.plan-price .side{display:flex;flex-direction:column;font-size:26px;line-height:1}
.plan-price .side small{font-size:15px;margin-bottom:6px}
.plan-features{list-style:none;padding:14px 0 0 20px;font-family:"Open Sans",Arial,sans-serif;font-size:14.5px;color:#333}
.plan-features li{height:48px;line-height:48px;position:relative;padding-left:29px}
.plan-features li::before{content:"";position:absolute;left:2px;top:21px;border-left:5px solid #555;border-top:3.5px solid transparent;border-bottom:3.5px solid transparent}
.plan-signup{position:absolute;left:20px;bottom:10px;width:200px;height:32px;border-radius:5px;background:linear-gradient(180deg,#3b3b3b,#121212);color:var(--white);font-size:15px;display:flex;align-items:center;padding-left:56px}
.plan-signup svg{position:absolute;right:8px;top:7px}
.plan--big .plan-signup{bottom:22px}

/* features */
.divider{left:132px;top:1870px;width:936px;height:1px;background:var(--rule)}
.feature-card{top:1905px;width:446px;height:162px;background:var(--white);box-shadow:0 1px 6px rgba(0,0,0,.15);padding:16px 14px}
.feature-card--affiliate{left:132px}
.feature-card--rating{left:621px}
.feature-photo{position:absolute;left:14px;top:16px;width:89px;height:89px;border-radius:50%}
.feature-photo--affiliate{background:linear-gradient(135deg,#8aa4bd,#d8cbb6)}
.feature-photo--rating{background:linear-gradient(135deg,#a7b7c3,#d7e0a2)}
.feature-body{margin-left:114px}
.feature-body h4{font-size:16px;font-weight:400;color:var(--orange);text-transform:uppercase;margin-top:3px}
.feature-body p{font-size:11px;line-height:22px;color:var(--light-grey);margin-top:8px}
.feature-body a{color:var(--orange);text-decoration:none;text-transform:uppercase}

/* ad banner */
.ad-banner{left:226px;top:2105px;width:748px;height:145px;background:linear-gradient(90deg,#111 0,#1b1b1b 45%,#5d6b4a 60%,#c98d3a 80%,#6f7d3f 100%);overflow:hidden}
.ad-banner .ad-head{position:absolute;left:16px;top:10px;font-family:"Open Sans",Arial,sans-serif;font-size:31px;color:var(--white)}
.ad-banner .ad-sub{position:absolute;left:90px;top:56px;font-size:12.5px;line-height:17px;color:#ddd}
.ad-strip{position:absolute;left:0;top:107px;width:748px;height:38px;background:linear-gradient(90deg,#eee 0,#ddd 60%,rgba(0,0,0,0) 61%)}
.ad-badge{position:absolute;top:112px;width:28px;height:28px;border-radius:50%;background:#6c5a9c}
.ad-badge--a{left:18px;background:#9a9a9a}
.ad-badge--b{left:90px}
.ad-date{position:absolute;right:10px;top:114px;text-align:right;font-size:11px;line-height:14px;color:var(--white)}

/* footer */
.footer{left:0;top:2297px;width:1200px;height:176px;background:var(--dark)}
.social-foot{left:153px;top:2336px;display:flex;gap:9px}
.social-foot span{width:30px;height:30px;border:2px solid #8f8f8f}
.newsletter-label{left:397px;top:2340px;font-family:"Open Sans",Arial,sans-serif;font-size:19px;color:#9a9a9a}
.newsletter-rule{left:511px;top:2333px;width:1px;height:40px;background:#555}
.newsletter-text{left:530px;top:2335px;font-size:10px;line-height:19px;color:#9a9a9a}
.newsletter-field{left:801px;top:2337px;width:249px;height:38px;background:#e9e9e9;display:flex;align-items:center;padding-left:10px;font-size:10px;color:#999;gap:10px}
.newsletter-field svg:last-child{margin-left:auto;margin-right:12px}
.copyright{left:0;top:2427px;width:1200px;text-align:center;font-size:11px;color:#bbb}
.bottom-rule{left:0;top:2468px;width:1200px;height:5px;background:var(--orange)}
</style>
</head>
<body>

<div class="abs top-rule"></div>

<header>
  <div class="abs brand">
    <span class="brand-dot"></span>
    <span class="brand-name">Fixy Fellas</span>
  </div>
  <div class="abs social-top" aria-label="Social links"><span></span><span></span><span></span><span></span><span></span></div>
  <nav class="abs main-nav">
    <a class="current" href="#">Home</a>
    <a href="#">About Us</a>
    <a href="#">Testimonials</a>
    <a href="#">Services</a>
    <a href="#">Prices</a>
    <a href="#">News</a>
    <a href="#" style="margin-right:0">Contact Us</a>
  </nav>
</header>

<section>
  <div class="abs hero" role="img" aria-label="Photo of a smiling contractor in a hard hat and safety vest drilling into a wooden frame inside a house under renovation"></div>
  <div class="abs hero-caption">
    <h1>FIXY FELLAS</h1>
    <p>Sed ut perspiciatis unde omnis iste natus error sit voluptatem accusantium doloremque laudantium, totam rem aperiam</p>
  </div>
  <div class="abs hero-arrows">
    <svg width="14" height="24" viewBox="0 0 14 24"><path d="M12 2 3 12l9 10" fill="none" stroke="#fff" stroke-width="3"/></svg>
    <svg width="14" height="24" viewBox="0 0 14 24"><path d="m2 2 9 10-9 10" fill="none" stroke="#fff" stroke-width="3"/></svg>
  </div>
</section>

<section>
  <h2 class="abs welcome-title">WELCOME TO <span class="accent">FIXY FELLAS</span></h2>
  <p class="abs welcome-text">Sed ut perspiciatis unde omnis iste natus error sit voluptatem accusantium doloremque laudantium, totam rem aperiam, eaque ipsa quae ab illo inventore veritatis et quasi architecto beatae vitae dicta sunt explicabo. Nemo enim ipsam voluptatem quia voluptas sit aspernatur aut odit aut fugit, sed quia consequuntur magni dolores eos qui ratione voluptatem sequi nesciunt.</p>
</section>

<section>
  <h2 class="abs section-title blog-title">LATEST <span class="accent">BLOG</span></h2>
  <div class="abs blog-arrows">
    <svg width="10" height="12" viewBox="0 0 10 12"><path d="M7 2 3 6l4 4" fill="none" stroke="#aaa" stroke-width="1.6"/></svg>
    <svg width="10" height="12" viewBox="0 0 10 12"><path d="m3 2 4 4-4 4" fill="none" stroke="#aaa" stroke-width="1.6"/></svg>
  </div>
  <div class="abs blog-card blog-card--1" role="img" aria-label="Photo of a tape measure and hand tools on a workbench"></div>
  <div class="abs blog-overlay">
    <h3>NEQUE PORRO QUISQUAM</h3>
    <p>We are setting up online advertising cam<br>We &nbsp;of advertising campaign.</p>
    <div class="blog-tools">
      <span><svg width="14" height="14" viewBox="0 0 14 14"><circle cx="6" cy="6" r="4" fill="none" stroke="#555" stroke-width="1.8"/><path d="m9 9 4 4" stroke="#555" stroke-width="1.8"/></svg></span>
      <span><svg width="14" height="14" viewBox="0 0 14 14"><path d="M6 8 8 6M5 6 3 8a2 2 0 0 0 3 3l2-2M9 8l2-2a2 2 0 0 0-3-3L6 5" fill="none" stroke="#555" stroke-width="1.5"/></svg></span>
    </div>
  </div>
  <div class="abs blog-card blog-card--2" role="img" aria-label="Photo of a worker's tool belt with a hammer"></div>
  <div class="abs blog-label" style="left:467px">NEQUE PORRO QUISQUAM</div>
  <div class="abs blog-card blog-card--3" role="img" aria-label="Photo of a woman assembling furniture with a screwdriver"></div>
  <div class="abs blog-label" style="left:789px">NEQUE PORRO QUISQUAM</div>
</section>

<section>
  <div class="abs pricing-band"></div>
  <h2 class="abs pricing-title">PRICING TABLES</h2>

  <div class="abs plan plan--regular">
    <div class="plan-name">Regular Thinker</div>
    <div class="plan-price"><span class="cur">$</span><span class="num">0</span><span class="side"><small>.00</small>/MO</span></div>
    <ul class="plan-features">
      <li>10 Websites Cap</li><li>5TB Bandwidth Cap</li><li>80GB Space Storage</li><li>Domain Name Included</li><li>24/7 Unlimited Support</li>
    </ul>
    <div class="plan-signup">Sign Up<svg width="30" height="18" viewBox="0 0 30 18"><path d="M2 2l7 7-7 7M11 2l7 7-7 7M20 2l7 7-7 7" fill="none" stroke="#f07a1f" stroke-width="3.5"/></svg></div>
  </div>

  <div class="abs plan plan--big">
    <div class="plan-name">Big Thinker</div>
    <div class="plan-price"><span class="cur">$</span><span class="num">29</span><span class="side"><small>.95</small>/MO</span></div>
    <ul class="plan-features">
      <li>15 Websites Cap</li><li>10TB Bandwidth Cap</li><li>100GB Space Storage</li><li>Domain Name Included</li><li>24/7 Unlimited Support</li><li>Custom E-Mail</li>
    </ul>
    <div class="plan-signup">Sign Up<svg width="30" height="18" viewBox="0 0 30 18"><path d="M2 2l7 7-7 7M11 2l7 7-7 7M20 2l7 7-7 7" fill="none" stroke="#f07a1f" stroke-width="3.5"/></svg></div>
  </div>

  <div class="abs plan plan--frequent">
    <div class="plan-name">Frequent Thinker</div>
    <div class="plan-price"><span class="cur">$</span><span class="num">19</span><span class="side"><small>.95</small>/MO</span></div>
    <ul class="plan-features">
      <li>20 Websites Cap</li><li>50TB Bandwidth Cap</li><li>200GB Space Storage</li><li>Domain Name Included</li><li>24/7 Unlimited Support</li><li>Custom E-Mail</li>
    </ul>
    <div class="plan-signup">Sign Up<svg width="30" height="18" viewBox="0 0 30 18"><path d="M2 2l7 7-7 7M11 2l7 7-7 7M20 2l7 7-7 7" fill="none" stroke="#f07a1f" stroke-width="3.5"/></svg></div>
  </div>
</section>

<section>
  <div class="abs divider"></div>
  <article class="abs feature-card feature-card--affiliate">
    <div class="feature-photo feature-photo--affiliate" role="img" aria-label="Photo of a carpenter at work"></div>
    <div class="feature-body">
      <h4>Affiliate Program</h4>
      <p>Vero eos et accusamus et iusto odio dignissimos ducimus qui blanditiis praesentium voluptatum deleniti atque corr upti quos dolores et quas molestias excepturi sint occaecati cupiditate non provident..... <a href="#">Click Here</a></p>
    </div>
  </article>
  <article class="abs feature-card feature-card--rating">
    <div class="feature-photo feature-photo--rating" role="img" aria-label="Photo of a contractor talking with a homeowner"></div>
    <div class="feature-body">
      <h4>Contractor Rating System</h4>
      <p>Vero eos et accusamus et iusto odio dignissimos ducimus qui blanditiis praesentium voluptatum deleniti atque corr upti quos dolores et quas molestias excepturi sint occaecati cupiditate non provident..... <a href="#">Click Here</a></p>
    </div>
  </article>
</section>

<aside class="abs ad-banner" role="img" aria-label="Banner ad for a health summit with a city skyline and riverside park scene">
  <div class="ad-head">HCA - HEA SUMMIT 2014</div>
  <div class="ad-sub">Harbour Care Alliance &amp;<br>Harbour Educators Association</div>
  <div class="ad-strip"></div>
  <span class="ad-badge ad-badge--a"></span>
  <span class="ad-badge ad-badge--b"></span>
  <div class="ad-date">27th - 29th August, 2014<br>Riverside Convention Hall, North Bay</div>
</aside>

<footer>
  <div class="abs footer"></div>
  <div class="abs social-foot" aria-label="Social links"><span></span><span></span><span></span><span></span><span></span></div>
  <div class="abs newsletter-label">NewsLetter :</div>
  <div class="abs newsletter-rule"></div>
  <p class="abs newsletter-text">In venenatis neque a eros laoreet eu placerat erat suscipit.<br>Fusce cursus, erat et scelerisque condimentum</p>
  <div class="abs newsletter-field">
    <svg width="18" height="12" viewBox="0 0 18 12"><rect x="1" y="1" width="16" height="10" fill="none" stroke="#888" stroke-width="1.4"/><path d="m1 1 8 6 8-6" fill="none" stroke="#888" stroke-width="1.4"/></svg>
    <span>Enter Your Email Address</span>
    <svg width="8" height="12" viewBox="0 0 8 12"><path d="m2 2 4 4-4 4" fill="none" stroke="#999" stroke-width="1.5"/></svg>
  </div>
  <p class="abs copyright">© Copy Rights 2014 Fixy Fellas All Rights Reserved</p>
  <div class="abs bottom-rule"></div>
</footer>

</body>
</html>
```